Business software developers new website

We need to redesign our website. Our current website is http://www.plumvista.net/index.html, which is outdated and needs a new look. We moved out from web design and have concentrated more on the back end of the systems, for example, system support and security and cloud-based applications. Our major clients include both private and government sectors. We would like to see some designs that are all in one page, simple and clean. Prefer illustrator or obstructed images instead of real-life photos. Must look futuristic yet friendly. Attached the new logo for your references and good luck.

Target Market(s)

Medium to big company for their IT or data management. Either improve or upgrade their current system.

Industry/Entity Type

Business Software

Number of Pages Required

1 page

Colors

Designer to choose colors to be used in the design.

Requirements
Must have
• Simple and clean. Individual assets must be provided in the correct size and format(png or jpeg). Prefer Goggle fonts. Even though the logo color is red, grey and black, still prefer some modern colors that go well with red. When design, must consider the possibility to convert it into responsive.
Nice to have
• White background
Should not have
• real life photos, no slider

```html
<!DOCTYPE html>
<html lang="en">
<head>
<meta charset="UTF-8">
<title>plumvista.net — Business Software</title>
<link href="https://fonts.googleapis.com/css2?family=Poppins:wght@400;500;600;700;800&display=swap" rel="stylesheet">
<style>
:root{
  --navy:#15152b;
  --navy-2:#1d1d3a;
  --red:#e8333f;
  --red-dark:#c81f2c;
  --ink:#1a1a1a;
  --body:#6b6b78;
  --ghost:#e6e8f0;
  --white:#ffffff;
  --line:#e9e9ef;
}
*{margin:0;padding:0;box-sizing:border-box}
html,body{width:1200px;height:2761px;overflow:hidden;background:var(--white)}
body{font-family:'Poppins',sans-serif;color:var(--ink);position:relative}
.abs{position:absolute}
.backdrop{position:absolute;left:0;top:0;width:1200px;height:2761px}

/* nav */
.logo{font-weight:700;color:var(--white);font-size:28px;letter-spacing:-.5px;display:flex;align-items:center;gap:8px}
.logo .dot{width:10px;height:10px;border-radius:50%;background:var(--red)}
.site-logo{left:18px;top:18px}
.main-nav{left:438px;top:14px;display:flex;gap:20px;font-size:14px;color:var(--white);font-weight:500}
.main-nav .active{color:var(--red)}
.nav-btn{top:12px;height:26px;border-radius:13px;font-size:13px;font-weight:600;display:flex;align-items:center;justify-content:center;color:var(--white)}
.btn-login{left:1001px;width:88px;border:2px solid var(--white)}
.btn-signup{left:1095px;width:90px;background:var(--red)}

/* buttons */
.pill{height:32px;border-radius:16px;background:var(--red);color:var(--white);font-size:13px;font-weight:500;display:flex;align-items:center;padding-left:20px;box-shadow:0 6px 14px rgba(232,51,63,.3)}
.pill .arrow{position:absolute;right:5px;top:5px;width:22px;height:22px;border-radius:50%;background:var(--white);display:flex;align-items:center;justify-content:center}
.pill.light{background:var(--white);color:var(--ink);box-shadow:none}
.pill.light .arrow{background:var(--red)}

/* hero */
.hero-title{left:200px;top:92px;font-size:44px;line-height:50px;font-weight:700;color:var(--white)}
.hero-sub{left:200px;top:206px;font-size:12.5px;line-height:20px;color:var(--white);font-weight:500;width:420px}
.hero-cta{left:200px;top:276px;width:155px}
.hero-art{left:616px;top:55px;width:490px;height:377px;border-radius:24px;background:linear-gradient(140deg,#2c2f5c 0%,#3f4690 45%,#e8333f 100%);opacity:.85}

/* feature cards */
.feature{width:254px;height:212px;background:var(--white);border-radius:3px;box-shadow:0 8px 24px rgba(20,20,50,.14);text-align:center;padding-top:28px}
.feature.lift{box-shadow:0 8px 24px rgba(60,90,200,.22)}
.feature .icon{width:70px;height:70px;margin:0 auto 18px}
.feature h3{font-size:14px;font-weight:600;letter-spacing:.3px}
.feature p{font-size:10.5px;line-height:15px;color:var(--body);margin:6px auto 0;width:190px}
.intro-title{left:758px;top:598px;font-size:34px;font-weight:700}
.intro-copy{left:758px;top:651px;width:245px;font-size:10.5px;line-height:15.5px;color:var(--body)}
.intro-cta{left:758px;top:797px;width:155px}

/* section heads */
.ghost-word{left:0;width:1200px;text-align:center;font-weight:800;color:var(--ghost);font-size:140px;letter-spacing:2px;line-height:1}
.section-title{font-size:40px;font-weight:700}

/* expertise */
.service{width:260px}
.service .icon{width:36px;height:36px;margin-bottom:18px}
.service h4{font-size:11px;font-weight:700;line-height:14px;letter-spacing:.3px}
.service p{font-size:10px;line-height:14px;color:var(--body);margin-top:6px}

/* projects */
.project{top:1656px;height:291px;width:288px;border-radius:2px;box-shadow:0 6px 18px rgba(0,0,0,.15)}
.client{top:2066px;width:151px;height:105px;background:var(--white);border:1px solid var(--line);display:flex;align-items:center;justify-content:center;gap:8px;font-size:15px;font-weight:600;color:var(--ink)}
.client .mark{width:12px;height:12px;border-radius:50%;background:var(--ink)}

/* contact */
.hello{left:166px;top:2217px;width:441px;height:320px}
.hello-title{left:166px;top:2280px;width:441px;text-align:center;font-size:50px;line-height:48px;font-weight:700;color:var(--white)}
.hello-sub{left:166px;top:2391px;width:441px;text-align:center;font-size:16px;color:var(--white)}
.hello-cta{left:305px;top:2432px;width:152px}
.ready-title{left:644px;top:2262px;font-size:36px;line-height:40px;font-weight:700;color:var(--navy)}
.ready-copy{left:644px;top:2359px;width:350px;font-size:10.5px;line-height:15px;color:var(--body)}
.ready-cta{left:644px;top:2453px;width:156px}

/* footer */
.foot-links{left:199px;top:2586px;font-size:11px;line-height:18px;color:var(--white)}
.foot-head{font-size:13px;font-weight:600;color:var(--white)}
.foot-text{font-size:10px;line-height:13.5px;color:#c9c9d6;width:310px;margin-top:10px}
.phone{font-size:18px;color:var(--white);margin-top:14px}
.foot-rule{left:0;top:2686px;width:1200px;height:1px;background:rgba(255,255,255,.08)}
.footer-logo{left:199px;top:2709px}
.copyright{left:524px;top:2722px;font-size:11px;color:#b9b9c8}
.socials{left:915px;top:2722px;display:flex;gap:8px}
.socials span{width:10px;height:10px;border-radius:50%;background:#c9c9d6}
</style>
</head>
<body>

<svg class="backdrop" viewBox="0 0 1200 2761" aria-hidden="true">
  <path fill="#15152b" d="M0 0H1200V290C1060 300 720 330 630 470C540 610 320 640 140 700C70 724 25 760 0 810Z"/>
  <path fill="#15152b" d="M1200 1480C1060 1470 960 1560 930 1640C1090 1700 1125 1880 1125 2010C1125 2080 1150 2115 1200 2125Z"/>
  <path fill="#15152b" d="M0 2175C170 2180 250 2300 330 2420C430 2565 620 2545 820 2530C1010 2518 1150 2500 1200 2470V2761H0Z"/>
</svg>

<!-- navigation -->
<div class="abs logo site-logo">plumvista.net<span class="dot"></span></div>
<nav class="abs main-nav">
  <span class="active">HOME</span><span>OUR SERVICES</span><span>OUR CLIENTS</span><span>CONTACT US</span>
</nav>
<div class="abs nav-btn btn-login">LOG IN</div>
<div class="abs nav-btn btn-signup">SIGN UP</div>

<!-- hero -->
<h1 class="abs hero-title">GET A RETURN<br>ON TECHNOLGY</h1>
<p class="abs hero-sub">THE STANDARD CHUNK OF LOREM IPSUM USED SINCE THE 1500S IS REPRODUCED BELOW FOR THOSE INTERESTED.</p>
<div class="abs pill hero-cta">GET STARTED<span class="arrow"><svg width="10" height="10" viewBox="0 0 10 10"><path d="M3 1l4 4-4 4" stroke="#e8333f" stroke-width="2" fill="none"/></svg></span></div>
<div class="abs hero-art" role="img" aria-label="Isometric illustration of a team working on connected cloud and server platforms"></div>

<!-- features -->
<div class="abs feature" style="left:199px;top:462px">
  <div class="icon" role="img" aria-label="Lightbulb with circuit icon" style="border:3px solid var(--red);border-radius:50% 50% 30% 30%"></div>
  <h3>INNOVATION</h3><p>Discover new ways to use and improve technology</p>
</div>
<div class="abs feature lift" style="left:475px;top:495px">
  <div class="icon" role="img" aria-label="Gear in lightbulb icon" style="border:3px dashed var(--red);border-radius:50%"></div>
  <h3>INGENUITY</h3><p>Design clever and elegant experiences</p>
</div>
<div class="abs feature" style="left:199px;top:696px">
  <svg class="icon" viewBox="0 0 70 70" aria-hidden="true"><g fill="none" stroke="#e8333f" stroke-width="2.5"><rect x="8" y="48" width="8" height="16"/><rect x="22" y="40" width="8" height="24"/><rect x="36" y="32" width="8" height="32"/><rect x="50" y="22" width="8" height="42"/><path d="M4 44C24 38 44 26 62 6M54 6h8v8"/></g><path d="M2 66h66" stroke="#1a1a1a" stroke-width="2"/></svg>
  <h3>INSIGHTS</h3><p>Realize the power of data</p>
</div>
<div class="abs feature" style="left:475px;top:729px">
  <div class="icon" role="img" aria-label="Megaphone with ideas icon" style="border:3px solid var(--red);border-radius:12px"></div>
  <h3>IMAGINATION</h3><p>Confront and deal with technical problems</p>
</div>

<h2 class="abs intro-title">RETRN ON...</h2>
<p class="abs intro-copy">Lorem ipsum dolor sit amet, consectetur adipiscing elit. Ut rutrum diam a elit euismod ultrices. Sed sagittis, urna sed congue elementum, orci sapien pulvinar sapien, eu mollis magna lacus eu ex. Nam sit amet ante fermentum, pulvinar massa sit amet, pretium dolor. Vestibulum finibus purus at augue aliquet, sit amet eleifend sem.</p>
<div class="abs pill intro-cta">LEARN MORE<span class="arrow"><svg width="10" height="10" viewBox="0 0 10 10"><path d="M3 1l4 4-4 4" stroke="#e8333f" stroke-width="2" fill="none"/></svg></span></div>

<!-- expertise -->
<div class="abs ghost-word" style="top:980px">EXPERTISE</div>
<h2 class="abs section-title" style="left:0;width:1200px;text-align:center;top:1058px">OUR EXPERTISE</h2>

<div class="abs service" style="left:199px;top:1150px">
  <svg class="icon" viewBox="0 0 36 36" aria-hidden="true"><rect x="3" y="5" width="30" height="26" fill="none" stroke="#e8333f" stroke-width="2"/><path d="M3 11h30M13 17l-4 4 4 4M23 17l4 4-4 4" stroke="#1a1a1a" stroke-width="2" fill="none"/></svg>
  <h4>SOFTWARE<br>DEVELOPMENT</h4><p>Lorem ipsum dolor sit amet, consectetur adipiscing elit. Ut rutrum diammod ultrices. Sed sagittis, urna sed congue</p>
</div>
<div class="abs service" style="left:510px;top:1150px">
  <svg class="icon" viewBox="0 0 36 36" aria-hidden="true"><path d="M9 22a6 6 0 0 1 1-12 8 8 0 0 1 15 2 5 5 0 0 1 0 10Z" fill="none" stroke="#e8333f" stroke-width="2"/><path d="M12 22v8M18 22v10M24 22v8" stroke="#1a1a1a" stroke-width="2"/></svg>
  <h4>CLOUD<br>COMPUTING</h4><p>Lorem ipsum dolor sit amet, consectetur adipiscing elit. Ut rutrum diammod ultrices. Sed sagittis, urna sed congue</p>
</div>
<div class="abs service" style="left:822px;top:1150px">
  <svg class="icon" viewBox="0 0 36 36" aria-hidden="true"><path d="M18 3l13 5v9c0 8-6 13-13 16C11 30 5 25 5 17V8Z" fill="none" stroke="#e8333f" stroke-width="2"/><rect x="13" y="16" width="10" height="8" fill="none" stroke="#1a1a1a" stroke-width="2"/></svg>
  <h4>SYSTEM<br>SECURITY</h4><p>Lorem ipsum dolor sit amet, consectetur adipiscing elit. Ut rutrum diammod ultrices. Sed sagittis, urna sed congue</p>
</div>
<div class="abs service" style="left:199px;top:1306px">
  <svg class="icon" viewBox="0 0 36 36" aria-hidden="true"><g fill="none" stroke="#e8333f" stroke-width="2"><rect x="4" y="4" width="20" height="8"/><rect x="4" y="14" width="20" height="8"/><rect x="4" y="24" width="20" height="8"/></g><path d="M24 8h6v20h-6" stroke="#1a1a1a" stroke-width="2" fill="none"/></svg>
  <h4>WEBSITE<br>HOSTING</h4><p>Lorem ipsum dolor sit amet, consectetur adipiscing elit. Ut rutrum diammod ultrices. Sed sagittis, urna sed congue</p>
</div>
<div class="abs service" style="left:510px;top:1306px">
  <svg class="icon" viewBox="0 0 36 36" aria-hidden="true"><rect x="4" y="6" width="22" height="16" fill="none" stroke="#e8333f" stroke-width="2"/><path d="M26 10l7-4v16l-7-4M10 22l2 10" stroke="#1a1a1a" stroke-width="2" fill="none"/></svg>
  <h4>DIGITAL<br>MARKETING</h4><p>Lorem ipsum dolor sit amet, consectetur adipiscing elit. Ut rutrum diammod ultrices. Sed sagittis, urna sed congue</p>
</div>
<div class="abs service" style="left:822px;top:1306px">
  <svg class="icon" viewBox="0 0 36 36" aria-hidden="true"><rect x="4" y="4" width="28" height="28" fill="none" stroke="#1a1a1a" stroke-width="2"/><path d="M10 18l6 6 11-12" stroke="#e8333f" stroke-width="2.5" fill="none"/></svg>
  <h4>WEBSITE<br>SECURITY</h4><p>Lorem ipsum dolor sit amet, consectetur adipiscing elit. Ut rutrum diammod ultrices. Sed sagittis, urna sed congue</p>
</div>

<!-- projects -->
<div class="abs ghost-word" style="top:1490px">PROJECTS</div>
<h2 class="abs section-title" style="left:200px;top:1565px">OUR PROJECTS</h2>
<div class="abs project" style="left:0;background:linear-gradient(180deg,#1c1410 0%,#6b4a2e 45%,#2a1d14 100%)" role="img" aria-label="Restaurant website project preview"></div>
<div class="abs project" style="left:304px;background:linear-gradient(180deg,#eef2f7 0%,#8fb3d9 40%,#f4f6f9 70%)" role="img" aria-label="Association website project preview"></div>
<div class="abs project" style="left:609px;background:linear-gradient(180deg,#f3f1ee 0%,#d8c6a6 40%,#2a3e74 85%)" role="img" aria-label="Recruitment website project preview"></div>
<div class="abs project" style="left:913px;background:linear-gradient(180deg,#c82027 0%,#b68a5e 35%,#f4f4f4 60%)" role="img" aria-label="Driving school website project preview"></div>
<div class="abs pill" style="left:817px;top:1982px;width:182px;padding-left:20px">VIEW ALL PROJECTS<span class="arrow"><svg width="10" height="10" viewBox="0 0 10 10"><path d="M3 1l4 4-4 4" stroke="#e8333f" stroke-width="2" fill="none"/></svg></span></div>

<div class="abs client" style="left:199px"><span class="mark"></span>Velmora</div>
<div class="abs client" style="left:363px"><span class="mark"></span>Ridgeway Trails</div>
<div class="abs client" style="left:527px"><span class="mark"></span>Northpeak Group</div>
<div class="abs client" style="left:691px"><span class="mark"></span>Quillstack</div>
<div class="abs client" style="left:853px"><span class="mark"></span>Corvane</div>

<!-- contact -->
<svg class="abs hello" viewBox="0 0 441 320" aria-hidden="true"><path fill="#e8333f" d="M60 18C140 -10 190 40 230 32C300 16 380 -8 420 40C460 90 430 170 380 230C330 290 260 322 200 318C130 314 50 280 20 210C-10 140 -5 45 60 18Z"/></svg>
<div class="abs hello-title">SAY<br>HELLO.</div>
<div class="abs hello-sub">Tell us about your project.</div>
<div class="abs pill light hello-cta">CONTACT US<span class="arrow"><svg width="10" height="10" viewBox="0 0 10 10"><path d="M3 1l4 4-4 4" stroke="#fff" stroke-width="2" fill="none"/></svg></span></div>

<h2 class="abs ready-title">READY?<br>SET. PLUMVISTA.NET</h2>
<p class="abs ready-copy">Lorem ipsum dolor sit amet, consectetur adipiscing elit. Ut rutrum diam a elit euismod ultrices. Sed sagittis, urna sed congue elementum, orci sapien pulvinar sapien, eu mollis magna lacus eu ex. Nam sit amet ante fermentum, pulvinar massa sit amet, pretium dolor. Vestibulum finibus purus at augue aliquet.</p>
<div class="abs pill ready-cta">GET STARTED<span class="arrow"><svg width="10" height="10" viewBox="0 0 10 10"><path d="M3 1l4 4-4 4" stroke="#e8333f" stroke-width="2" fill="none"/></svg></span></div>

<!-- footer -->
<ul class="abs foot-links" style="list-style:none">
  <li>HOME</li><li>OUR SERVICES</li><li>OUR CLIENTS</li><li>CONTACT US</li>
</ul>
<div class="abs" style="left:316px;top:2586px">
  <div class="foot-head">Philosophy</div>
  <p class="foot-text">As web developers, we understand that a powerful and functional web site is a vital component of modern day marketing for companies of today. This is why our web site development team work with all of our clients to ensure their web site design will deliver to their target market.</p>
</div>
<div class="abs" style="left:677px;top:2586px">
  <div class="foot-head">Office Number:</div>
  <div class="phone">+61 7 5550 1842</div>
</div>
<div class="abs" style="left:859px;top:2586px">
  <div class="foot-head">Mobile number:</div>
  <div class="phone">+61 0491 570 318</div>
</div>
<div class="abs foot-rule"></div>
<div class="abs logo footer-logo">plumvista.net<span class="dot"></span></div>
<div class="abs copyright">Copyright 2019 | Plumvista.net</div>
<div class="abs socials"><span></span><span></span><span></span><span></span><span></span></div>

</body>
</html>
```